Personalised Poetry business needs a business card designed

I am a writer that specialises in personalised poetry for people for significant life events.
I want a business card that stands out and portrays class and professionalism but is also welcoming & indicates warmth and honesty.
I'm happy with the logo that was designed for me, I would like to see it in raised print on the business card. I am open to suggestions on colours but think perhaps gold or silver writing for the logo would look good. I would like just the logo and my name and contact details on the front of the card. On the back of the card, I would like a list of the different events I provide poems for I will upload a photo of my current business card for reference. My current logo has a shading behind it that I don't like, I just want the words of the logo without any background colour

Target Market(s)

People wanting to provide a unique gift to someone special in their life

Industry/Entity Type

Writer

Contact Information for Business Card

Logo, my name and contact details on the front and a list of all the events I write poetry for on the back

Font styles to use
Script

Requirements
Must have
• I would like to see the logo, if possible, in a raised type of print on the card so that you can feel the actual words. I would like to have a glossy finish to the card and be able to print it on good quality board
Should not have
• The shading that is currently behind the logo on my current business card

```html
<!DOCTYPE html>
<html lang="en">
<head>
<meta charset="UTF-8">
<title>Lines for Always — Business Card</title>
<link rel="stylesheet" href="https://fonts.googleapis.com/css2?family=Poppins:wght@300;400;600&family=Great+Vibes&display=swap">
<style>
  :root {
    --backdrop: #1f1f1f;
    --card: #363636;
    --band: #ffffff;
    --ink-light: #ffffff;
    --ink-soft: #cfcfcf;
    --ink-dark: #111111;
    --art-tone-a: #e6e6e6;
    --art-tone-b: #bdbdbd;
  }
  * { box-sizing: border-box; margin: 0; padding: 0; }
  html, body { width: 1200px; height: 780px; overflow: hidden; }
  body {
    background: var(--backdrop);
    font-family: "Poppins", sans-serif;
    display: flex;
    align-items: center;
    justify-content: center;
    gap: 40px;
  }
  .card {
    position: relative;
    width: 540px;
    height: 310px;
    background: var(--card);
    color: var(--ink-light);
    overflow: hidden;
    border-radius: 3px;
  }

  /* Brand lockup */
  .brand {
    position: absolute;
    display: flex;
    flex-direction: column;
    align-items: center;
  }
  .brand-name {
    display: flex;
    align-items: center;
    gap: 10px;
    font-weight: 400;
    color: var(--ink-light);
    white-space: nowrap;
  }
  .brand-dot {
    width: 14px; height: 14px;
    border-radius: 50%;
    background: var(--ink-light);
  }
  .brand-tagline {
    font-weight: 300;
    color: var(--ink-soft);
    letter-spacing: 0.5px;
  }

  /* Front */
  .card-front .brand { top: 44px; left: 200px; width: 280px; }
  .card-front .brand-name { font-size: 28px; }
  .card-front .brand-tagline { font-size: 13px; margin-top: 4px; }

  .info-band {
    position: absolute;
    left: 0; right: 0;
    top: 160px;
    height: 92px;
    background: var(--band);
    color: var(--ink-dark);
    display: flex;
    align-items: center;
    padding: 0 22px;
  }
  .person { width: 170px; }
  .person-name { font-size: 24px; line-height: 1.1; }
  .person-name .first { font-weight: 600; }
  .person-name .last { font-weight: 400; }
  .person-role { font-size: 12px; font-weight: 600; margin-top: 3px; }
  .writing-art {
    width: 78px;
    height: 78px;
    margin: 0 16px 0 6px;
    background: linear-gradient(135deg, var(--art-tone-a), var(--art-tone-b));
    border-radius: 4px;
  }
  .contact-list { list-style: none; font-size: 12.5px; font-weight: 400; }
  .contact-list li { display: flex; align-items: center; gap: 8px; line-height: 1.9; }
  .contact-list svg { width: 13px; height: 13px; flex: none; }

  .web-line {
    position: absolute;
    top: 268px;
    left: 30px;
    display: flex;
    align-items: center;
    gap: 8px;
    font-size: 13px;
    font-weight: 400;
  }
  .web-line svg { width: 13px; height: 13px; }

  /* Back */
  .card-back .brand { top: 30px; left: 110px; width: 320px; }
  .card-back .brand-name { font-size: 32px; }
  .card-back .brand-tagline { font-size: 15px; margin-top: 4px; }
  .events {
    position: absolute;
    top: 132px;
    left: 0; right: 0;
    text-align: center;
  }
  .events-heading {
    font-family: "Great Vibes", cursive;
    font-size: 26px;
    font-weight: 400;
    margin-bottom: 4px;
  }
  .event-list { list-style: none; font-size: 14px; font-weight: 400; line-height: 1.6; }
  .event-list li::before { content: "\2022"; margin-right: 8px; }
</style>
</head>
<body>

  <section class="card card-front" aria-label="Card front">
    <div class="brand">
      <div class="brand-name"><span class="brand-dot"></span>Lines for Always</div>
      <div class="brand-tagline">Personalised Poetry</div>
    </div>

    <div class="info-band">
      <div class="person">
        <div class="person-name"><span class="first">Marcus</span> <span class="last">Ellery</span></div>
        <div class="person-role">Writer &amp; Owner</div>
      </div>
      <div class="writing-art" role="img" aria-label="Line drawing of a hand writing with a fountain pen"></div>
      <ul class="contact-list">
        <li>
          <svg viewBox="0 0 24 24" fill="currentColor" aria-hidden="true"><path d="M6.6 10.8a15.1 15.1 0 0 0 6.6 6.6l2.2-2.2a1 1 0 0 1 1-.25 11.4 11.4 0 0 0 3.6.57 1 1 0 0 1 1 1V20a1 1 0 0 1-1 1A17 17 0 0 1 3 4a1 1 0 0 1 1-1h3.5a1 1 0 0 1 1 1c0 1.25.2 2.45.57 3.6a1 1 0 0 1-.25 1z"/></svg>
          0400 381 627
        </li>
        <li>
          <svg viewBox="0 0 24 24" fill="none" stroke="currentColor" stroke-width="2" aria-hidden="true"><rect x="3" y="5" width="18" height="14" rx="1"/><path d="M3 6l9 7 9-7"/></svg>
          marcus@linesforalways.com
        </li>
      </ul>
    </div>

    <div class="web-line">
      <svg viewBox="0 0 24 24" fill="none" stroke="currentColor" stroke-width="2" aria-hidden="true"><circle cx="12" cy="12" r="9"/><path d="M3 12h18M12 3c3 3.5 3 14.5 0 18M12 3c-3 3.5-3 14.5 0 18"/></svg>
      www.linesforalways.com
    </div>
  </section>

  <section class="card card-back" aria-label="Card back">
    <div class="brand">
      <div class="brand-name"><span class="brand-dot"></span>Lines for Always</div>
      <div class="brand-tagline">Personalised Poetry</div>
    </div>

    <div class="events">
      <h2 class="events-heading">Momentous Life Events Personalised in Poetry</h2>
      <ul class="event-list">
        <li>Valentines Day</li>
        <li>Funerals &amp; Eulogies</li>
        <li>Birthdays &amp; Christmas</li>
        <li>Weddings &amp; Anniversaries</li>
        <li>Retirements, Business &amp; Corporate Events</li>
      </ul>
    </div>
  </section>

</body>
</html>
```